IT Network Consultancy - Business Card

kelbrin systems is a IT network consultancy based in London. We're looking for a smart, modern and professional business card design. Our website is here: www.kelbrinsystems.co.uk

Key things that should be included on the card (with examples):

Company Logo
Name
Position / Job Title: Network Consultant
Mobile Phone Number: +44 (0) 7700 900418
Land Line: +44 (0) 1632 960735
Email Address: name@kelbrinsystems.co.uk
Web Site URL: www.kelbrinsystems.co.uk

Target Market(s)

Large enterprise / global companies / corporates

Industry/Entity Type

Business

Requirements
Must have
• Incorporate our logo - which is attached to the project. They are in AI format (can be opened in Inkscape).

The design should be double sided and fit on a UK standard 85mm × 55mm card and be in a format that retains the quality when printed.
Nice to have
• The project does not have to conform to the colour of our website but this should give you inspiration of the style we like.
Should not have
• Bright colours. Pictures are not necessary.

```html
<!DOCTYPE html>
<html lang="en">
<head>
<meta charset="utf-8">
<title>kelbrin systems – Business Card</title>
<link rel="stylesheet" href="https://fonts.googleapis.com/css2?family=Open+Sans:wght@300;400;700&display=swap">
<style>
  :root {
    --page-bg: #f2f2f0;
    --front-bg: #1f2a36;
    --front-bg-deep: #18222d;
    --front-logo: #b7bcc3;
    --front-tagline: #f1f3f5;
    --pattern-dark: rgba(120, 135, 150, 0.16);
    --back-bg: #d3d3d3;
    --back-bg-light: #dedede;
    --pattern-light: rgba(255, 255, 255, 0.35);
    --back-text: #1b1b1b;
    --card-shadow: 0 6px 18px rgba(0, 0, 0, 0.28);
  }

  * { box-sizing: border-box; margin: 0; padding: 0; }

  html, body {
    width: 1200px;
    height: 900px;
    overflow: hidden;
  }

  body {
    background: var(--page-bg);
    font-family: "Open Sans", Tahoma, sans-serif;
    position: relative;
  }

  .card {
    position: absolute;
    width: 560px;
    height: 362px;
    overflow: hidden;
    box-shadow: var(--card-shadow);
  }

  /* Front side */
  .card--front {
    left: 70px;
    top: 80px;
    background: linear-gradient(135deg, var(--front-bg) 0%, var(--front-bg-deep) 100%);
  }

  .card--front .node-pattern {
    position: absolute;
    inset: 0;
    background: radial-gradient(ellipse 70% 60% at 55% 35%, var(--pattern-dark) 0%, transparent 75%);
  }

  .brand {
    position: absolute;
    left: 40px;
    top: 136px;
    display: flex;
    align-items: center;
    gap: 16px;
  }

  .brand__dot {
    width: 44px;
    height: 44px;
    border-radius: 50%;
    background: var(--front-logo);
  }

  .brand__name {
    font-weight: 300;
    font-size: 50px;
    letter-spacing: 2px;
    color: var(--front-logo);
    text-transform: uppercase;
    line-height: 1;
  }

  .tagline {
    position: absolute;
    left: 118px;
    top: 232px;
    font-size: 15px;
    font-weight: 400;
    letter-spacing: 0.6px;
    color: var(--front-tagline);
    text-transform: uppercase;
  }

  /* Back side */
  .card--back {
    left: 570px;
    top: 458px;
    background: linear-gradient(160deg, var(--back-bg-light) 0%, var(--back-bg) 100%);
    color: var(--back-text);
  }

  .card--back .node-pattern {
    position: absolute;
    inset: 0;
    background: radial-gradient(ellipse 55% 55% at 70% 45%, var(--pattern-light) 0%, transparent 75%);
  }

  .contact {
    position: absolute;
    left: 0;
    right: 0;
    top: 26px;
    text-align: center;
    padding-left: 60px;
    font-size: 21px;
    line-height: 1.38;
  }

  .contact strong { font-weight: 700; }

  .contact__name { margin-bottom: 34px; }

  .contact__group + .contact__group { margin-top: 34px; }
</style>
</head>
<body>

  <section class="card card--front" aria-label="Business card front">
    <div class="node-pattern" role="img" aria-label="Faint network node pattern of connected circles"></div>
    <div class="brand">
      <span class="brand__dot"></span>
      <span class="brand__name">kelbrin systems</span>
    </div>
    <p class="tagline">Challenge the status quo</p>
  </section>

  <section class="card card--back" aria-label="Business card back">
    <div class="node-pattern" role="img" aria-label="Faint network node pattern of connected circles"></div>
    <div class="contact">
      <p class="contact__name"><strong>Alex Marlow</strong>, Network Consultant</p>
      <div class="contact__group">
        <p>Mobile: <strong>+44 (0) 7700 900418</strong></p>
        <p>Land Line: <strong>+44 (0) 1632 960735</strong></p>
      </div>
      <div class="contact__group">
        <p>Email: <strong>name@kelbrinsystems.co.uk</strong></p>
        <p>Web: <strong>www.kelbrinsystems.co.uk</strong></p>
      </div>
    </div>
  </section>

</body>
</html>
```